ちょっと急いでおりまして、
当方デザインをする時間がないので、
アウトソーシングしたいと思います。

文章、と構成だけを作りましたので、
宜しければ、お願い致します。

TAVELIA JAPAN で使用する、
お客さまにブランディングするための、
青嶺かやどり の パンフレットです。

PDFで、説明文を記載致しますので、
また見ておいて下さい。

画像素材も、添付させて頂きます。
「青嶺かやどり・かやたまご」を使うフォントは、
明朝体です。アウトラインしたデータも
添付いたします。それを活用下さい。

A4サイズ (裏・表)
両面カラーでで作っていただけると幸いです。

※もしかすると、A0サイズで引き伸ばしてつかうかもしれません。
どうぞよろしくお願い致します。

何か御不明な点がございましたら、お気軽に
ご質問ください。

当社青嶺かやどりの商品ページです。
参考にして下さい。
http://item.shopmarket-example.jp/poultry-hoshino/20004681/

青嶺かやどり協議会の ページです。
http://www.kayadori-example.com/
素材を添付いたします。レイヤーを使っておりますので、分解してください。
このページにある

の画像のような感じで、要約していただけると
幸いです。
画像を追加いたしました。
タイトルが、4Aに なってました。

すみません。A4ポスターです。
循環型の 111 のような 感じで、

ぐるっと 回る ように わかりやすく つくって頂けると幸いです。
かやどりの アニメーションデータは、

aiファイル イラストレーターの
かやたまご に 入っています。

レイヤーで組んでいますが、それを修正して作って下さい。
素材 画像を追加いたしました。
素材追加いたします。

111、222、333、444画像は、見本画像です。
イメージの参考になるかも?と思いまして、
かやどり からでる 副産物の 鶏糞堆肥もっこもこ の画像を 追加いたします。

裏側の、一番重要な情報を綺麗にまとめてくださりました。
そして、私達が やっていることに対して 共感頂けたことが大きかったです。
少し修正頂きたい部分がありますので、御連絡頂けると幸いです。

皆様 急な対応、ありがとうございます。
10件も御応募いただけるとは思っても居なかったのと、
そして、みなさんからの提案が本当に良かったので。
こちらとしても 悩ましかったです。
御提案くださった皆様。本当に、ありがとうございましたm(__)m

```html
<!DOCTYPE html>
<html lang="ja">
<head>
<meta charset="utf-8">
<title>青嶺かやどり かやたまご</title>
<link href="https://fonts.googleapis.com/css2?family=Shippori+Mincho+B1:wght@700;800&family=M+PLUS+Rounded+1c:wght@400;700;800&display=swap" rel="stylesheet">
<style>
:root{
  --bg:#f6b3cb;
  --bg-light:#fbd6e3;
  --red:#d8173f;
  --pink:#e8437a;
  --deep:#b8124a;
  --ink:#3a2a30;
  --white:#ffffff;
  --gold:#d9a928;
}
*{margin:0;padding:0;box-sizing:border-box}
html,body{width:857px;height:1200px;overflow:hidden}
body{font-family:"M PLUS Rounded 1c",sans-serif;color:var(--ink)}
.poster{position:relative;width:857px;height:1200px;overflow:hidden;
  background:radial-gradient(ellipse at 35% 40%,var(--bg-light) 0%,var(--bg) 70%)}
.mascot{position:absolute;left:160px;top:470px;width:310px;height:280px;border-radius:50% 50% 45% 45%;z-index:1;
  background:radial-gradient(circle at 50% 45%,#ffffff 0%,#fde8ef 55%,rgba(246,179,203,0) 75%)}
.title{position:absolute;z-index:2;font-family:"Shippori Mincho B1",serif;font-weight:800;
  font-size:80px;line-height:1;display:flex;flex-direction:column;align-items:center}
.title span{display:block;height:86px}
.title .red{color:var(--red)}
.title .pink{color:var(--pink)}
.title-main{left:205px;top:30px}
.title-sub{left:105px;top:170px}
.tagline{position:absolute;z-index:2;left:300px;top:170px;writing-mode:vertical-rl;
  font-size:11.5px;line-height:1.35;color:var(--deep);height:220px}
.tagline b{display:block;font-size:12.5px}
.headline{position:absolute;left:455px;top:70px;width:380px;font-family:"Shippori Mincho B1",serif;
  font-weight:800;line-height:1.2}
.headline .l1{font-size:36px;color:var(--red)}
.headline .l2{font-size:38px;color:var(--pink)}
.feature-label{position:absolute;left:470px;top:196px;background:var(--pink);color:var(--white);
  font-weight:700;font-size:15px;padding:4px 22px;border-radius:16px}
.features{position:absolute;left:470px;top:236px;width:365px;list-style:none}
.features li{display:flex;gap:10px;align-items:flex-start;font-size:14.5px;line-height:1.4;margin-bottom:11px;font-weight:700}
.num{flex:0 0 28px;height:28px;border-radius:50%;background:var(--pink);color:var(--white);
  font-size:16px;font-weight:800;display:flex;align-items:center;justify-content:center}
.origin-title{position:absolute;left:470px;top:438px;display:flex;gap:8px;align-items:center;
  font-size:21px;font-weight:800;color:var(--pink)}
.origin{position:absolute;left:500px;top:478px;width:330px;font-size:14px;line-height:1.75;font-weight:700}
.origin p{margin-bottom:10px}
.origin .hl{color:var(--red)}
.badges{position:absolute;left:28px;top:765px;display:flex;gap:18px}
.badge{width:112px;height:112px;border-radius:50%;
  background:radial-gradient(circle at 40% 35%,#f7e08a,var(--gold) 70%)}
.awards{position:absolute;left:28px;top:892px;width:400px;font-size:12.5px;line-height:1.6;font-weight:700}
.awards h3{font-size:15px;color:var(--deep);margin-bottom:4px}
.ranking{position:absolute;left:455px;top:842px;width:380px;font-size:12.5px;line-height:1.6;font-weight:700}
.ranking h3{font-size:14px;color:var(--deep);margin-bottom:4px}
.ranking ul{list-style:none}
.ranking li::before{content:"● ";color:var(--pink)}
.footer{position:absolute;left:0;top:1090px;width:857px;height:110px;background:var(--deep);
  color:var(--white);display:flex;align-items:center;padding:0 24px;gap:22px}
.footer .ask{font-size:15px;font-weight:700;line-height:1.4;width:200px}
.footer .org{display:flex;align-items:center;gap:10px;font-size:15px;font-weight:700;line-height:1.5}
.footer .mark{width:34px;height:34px;border-radius:50%;background:var(--white)}
.footer .org small{display:block;font-size:12px;font-weight:400}
.footer .office{margin-left:auto;font-size:12px;line-height:1.5;text-align:left}
.footer .tel{font-size:18px;font-weight:800}
</style>
</head>
<body>
<main class="poster">
  <div class="mascot" role="img" aria-label="かやどりとかやたまごのキャラクターイラスト"></div>

  <h1 class="title title-main" aria-label="青嶺かやどり かやたまご">
    <span class="red">青</span><span class="red">嶺</span><span class="pink">か</span><span class="red">や</span><span class="pink">ど</span><span class="red">り</span>
  </h1>
  <div class="title title-sub" aria-hidden="true">
    <span class="pink">か</span><span class="red">や</span><span class="pink">た</span><span class="red">ま</span><span class="pink">ご</span>
  </div>
  <p class="tagline"><b>Aomine Kayadori</b>The healthy chicken raised with care in the green mountains of Japan, and its eggs.</p>

  <div class="headline"><div class="l1">青嶺かやどり、</div><div class="l2">最大の自慢は健康!</div></div>

  <div class="feature-label">青嶺かやどりの特徴</div>
  <ol class="features">
    <li><span class="num">1</span>青嶺の梅酢を飲ませた贅沢な鶏</li>
    <li><span class="num">2</span>梅酢効果で免疫力アップ、抗酸化力アップ!病気にかかりにくい健康な鶏</li>
    <li><span class="num">3</span>かやどりは歯ごたえがあり、肉質や香りがよく、うま味がひきたつ</li>
    <li><span class="num">4</span>梅酢効果でコクがあり適度な弾力があるのでやわらかくうま味がある</li>
  </ol>

  <h2 class="origin-title"><svg width="22" height="22" viewBox="0 0 22 22"><circle cx="11" cy="11" r="10" fill="#e8437a"/><circle cx="11" cy="11" r="3" fill="#fff"/></svg>かやどりがはじまった経緯</h2>
  <div class="origin">
    <p>青嶺地域は梅干の生産がさかんで、梅干を作る工程で毎年たくさんの梅酢が生まれます。</p>
    <p>昔から梅酢には健康を支える力があるといわれ、これを鶏に与える試みがはじまりました。</p>
    <p>その結果、元気で病気にかかりにくい鶏が育ち、<span class="hl">「青嶺かやどり」</span><span class="hl">「青嶺かやたまご」</span>が誕生しました。</p>
  </div>

  <div class="badges">
    <div class="badge" role="img" aria-label="受賞記念バッジ"></div>
    <div class="badge" role="img" aria-label="受賞記念バッジ"></div>
  </div>
  <div class="awards">
    <h3>■食の総合見本市で各賞受賞</h3>
    <p>「ふるさと食肉アワード2008」にて最優秀賞を受賞。<br>全国の出品の中から味と品質が高く評価されました。</p>
  </div>

  <div class="ranking">
    <h3>■女性の暮らしを応援するサイト「ウィメンズデイリー」の</h3>
    <p>企画「産地からのお取り寄せランキング」にて</p>
    <ul>
      <li>全国から集まった商品の中から選出</li>
      <li>味、パッケージ、価格を総合的に評価</li>
      <li>かやどりが鶏肉部門で第1位を獲得</li>
    </ul>
  </div>

  <footer class="footer">
    <p class="ask">かやどり・かやたまごに関するお問い合わせは</p>
    <div class="org"><span class="mark"></span><div>青嶺かやどり・かやたまご協議会<small>http://www.kayadori-example.com/</small></div></div>
    <div class="office">事務局 株式会社星野ポートリー内<br>〒649-0000 架空県青嶺郡みどり町1-2-3<br><span class="tel">TEL 0739-41-2285</span></div>
  </footer>
</main>
</body>
</html>
```